Website for business consultancy - bright and happy feel needed

I need a website with 3/4 pages. I want the first page designed first and the rest will be easy. I need some pictures but none with corporate looking people. I need links to chatterbox and careerweb. I need a contact form. I have samples of websites i like, fonts i like and I need a small logo also. I like simple, clean lines and I want a bright, happy and feminine feel. My audience are small businesses so I don't want them intimidated by new much of a corporate feel.
Updates

Project Deadline Extended Reason: I have not received a design that reflects what I believe the brief to be, therefore I am extending the deadline and increasing the amount to be paid. Added Thursday, October 13, 2016

Target Market(s)

Small medium size businesses who want to grow and need that help but they cannot afford a full time financial director.

Industry/Entity Type

Business Consultant

Number of Pages Required

4 page

Font styles to use
Other font styles liked:
• i can attach images

Colors
fcf0f6
e667a6
85cae6
ffffff
fbee3e

Requirements
Must have
• Link to chatterbox and career web
• Contact form linked to my email
• Pictures - full width images where required
• Colour
• Mobile ready
• Soft feminine feel to it
• I dont want it to look like a corporate business consultancy - much more marketing or interior deign feel
Nice to have
• I would like the 3 services I have in 3 boxes that you click and takes you to a place with more information on the service.
• pictures thinking outside of the box
• Can be wordpress if need be
Should not have
• pictures with too much of a corporate feel
• No pictures of coporate people at all
• i like the following websites
• www.pebblordo.co.uk and others that are attached in the documents with a feminine feel to them

```html
<!DOCTYPE html>
<html lang="en">
<head>
<meta charset="utf-8">
<title>Maura Lindell | Business Consultant</title>
<link rel="stylesheet" href="https://fonts.googleapis.com/css2?family=Libre+Baskerville&family=Montserrat:wght@400;600;700&display=swap">
<style>
  :root {
    --white: #ffffff;
    --ink: #2f2f2f;
    --nav-grey: #5a5a5a;
    --muted-grey: #6e6e6e;
    --teal: #7fcdc8;
    --teal-edge: #a9dcd8;
    --blush: #fcf0f6;
    --rose: #e667a6;
    --rose-deep: #c9558f;
    --sky: #85cae6;
    --sky-deep: #4f9dbf;
    --sun: #fbee3e;
    --hero-veil: rgba(70, 45, 70, 0.22);
    --card-shade: rgba(60, 45, 65, 0.30);
    --card-frame: rgba(255, 255, 255, 0.9);
  }
  * { box-sizing: border-box; margin: 0; padding: 0; }
  html, body {
    width: 1200px;
    height: 659px;
    overflow: hidden;
    background: var(--white);
    font-family: "Montserrat", Arial, sans-serif;
  }
  .page {
    position: relative;
    width: 1200px;
    height: 659px;
    overflow: hidden;
  }

  /* Header */
  .site-header {
    position: absolute;
    top: 0; left: 0;
    width: 1200px;
    height: 87px;
    background: var(--white);
  }
  .call-line {
    position: absolute;
    top: 11px;
    left: 998px;
    font-size: 10px;
    letter-spacing: 0.5px;
    color: var(--muted-grey);
  }
  .brand-name {
    position: absolute;
    top: 28px;
    left: 109px;
    font-family: "Libre Baskerville", Georgia, serif;
    font-size: 40px;
    font-weight: 400;
    color: var(--ink);
    letter-spacing: 0.3px;
    white-space: nowrap;
  }
  .main-nav a {
    position: absolute;
    top: 59px;
    font-size: 11px;
    color: var(--nav-grey);
    text-decoration: none;
    text-transform: uppercase;
    letter-spacing: 0.2px;
    white-space: nowrap;
  }
  .nav-home { left: 481px; }
  .nav-marketing { left: 605px; }
  .nav-finance { left: 752px; }
  .nav-coach { left: 869px; }
  .nav-contact { left: 1029px; }

  .accent-band {
    position: absolute;
    top: 87px; left: 0;
    width: 1200px;
    height: 15px;
    background: var(--teal);
    border-top: 2px solid var(--teal-edge);
  }

  /* Hero */
  .hero {
    position: absolute;
    top: 102px; left: 0;
    width: 1200px;
    height: 513px;
  }
  .hero-photo {
    position: absolute;
    inset: 0;
    background:
      linear-gradient(var(--hero-veil), var(--hero-veil)),
      radial-gradient(ellipse 220px 170px at 790px 110px, rgba(133, 202, 230, 0.75), transparent 70%),
      radial-gradient(ellipse 240px 130px at 330px 70px, rgba(251, 238, 62, 0.35), transparent 70%),
      radial-gradient(ellipse 420px 200px at 600px 380px, rgba(252, 240, 246, 0.55), transparent 70%),
      linear-gradient(160deg, var(--rose-deep) 0%, var(--rose) 35%, #d9a0c6 60%, var(--sky) 82%, var(--sky-deep) 100%);
  }
  .hero-title {
    position: absolute;
    top: 164px;
    left: 190px;
    font-size: 41px;
    font-weight: 600;
    line-height: 47px;
    color: var(--white);
    text-transform: uppercase;
    letter-spacing: 0.3px;
    white-space: nowrap;
    text-shadow: 0 1px 8px rgba(60, 30, 60, 0.35);
  }
  .hero-button {
    position: absolute;
    top: 283px;
    left: 190px;
    width: 199px;
    height: 45px;
    border: 2px solid var(--white);
    border-radius: 3px;
    color: var(--white);
    font-size: 14px;
    letter-spacing: 0.5px;
    text-decoration: none;
    display: flex;
    align-items: center;
    justify-content: center;
    text-shadow: 0 1px 4px rgba(60, 30, 60, 0.3);
  }

  /* Service cards */
  .service-card {
    position: absolute;
    top: 513px;
    height: 160px;
    text-decoration: none;
    color: var(--white);
    text-align: center;
  }
  .card-photo {
    position: absolute;
    inset: 0;
  }
  .card-finance { left: 107px; width: 333px; }
  .card-marketing { left: 447px; width: 320px; }
  .card-business { left: 786px; width: 316px; }
  .card-finance .card-photo {
    background: linear-gradient(150deg, #d98cb5 0%, #b9779b 55%, #8a5a76 100%);
  }
  .card-marketing .card-photo {
    background: linear-gradient(160deg, #8fc6de 0%, #6ea7c2 55%, #527f98 100%);
  }
  .card-business .card-photo {
    background: linear-gradient(150deg, #d39bc0 0%, #9f8fb8 55%, #6e87a8 100%);
  }
  .card-frame {
    position: absolute;
    top: 8px; left: 11px; right: 11px; bottom: -10px;
    border: 1px solid var(--card-frame);
    background: var(--card-shade);
    padding: 34px 24px 0;
  }
  .card-title {
    font-size: 14px;
    font-weight: 700;
    text-transform: uppercase;
    margin-bottom: 6px;
  }
  .card-text {
    font-size: 10.5px;
    font-weight: 600;
    line-height: 13px;
    max-width: 196px;
    margin: 0 auto;
  }
</style>
</head>
<body>
<div class="page">
  <header class="site-header">
    <p class="call-line">Need a hand?Call me</p>
    <div class="brand-name">Maura Lindell</div>
    <nav class="main-nav">
      <a class="nav-home" href="#">Home</a>
      <a class="nav-marketing" href="#">Marketing</a>
      <a class="nav-finance" href="#">Finance</a>
      <a class="nav-coach" href="#">Business Coach</a>
      <a class="nav-contact" href="#">Contact</a>
    </nav>
  </header>
  <div class="accent-band"></div>

  <section class="hero">
    <div class="hero-photo" role="img" aria-label="Bright desk scene with an open ring planner, coloured pens and a glass vase of greenery"></div>
    <h1 class="hero-title">Not all businesses can<br>afford the best...</h1>
    <a class="hero-button" href="#">GET IN TOUCH</a>
  </section>

  <a class="service-card card-finance" href="#">
    <div class="card-photo" role="img" aria-label="Calculator, pen and financial papers on a desk"></div>
    <div class="card-frame">
      <h2 class="card-title">Finance</h2>
      <p class="card-text">Lorem ipsum dolor sit amet, consectetuer adipiscing elit. Aenean commodo ligula eget dolor.</p>
    </div>
  </a>
  <a class="service-card card-marketing" href="#">
    <div class="card-photo" role="img" aria-label="Laptop on a desk with hands typing"></div>
    <div class="card-frame">
      <h2 class="card-title">Marketing</h2>
      <p class="card-text">Lorem ipsum dolor sit amet, consectetuer adipiscing elit. Aenean commodo ligula eget dolor.</p>
    </div>
  </a>
  <a class="service-card card-business" href="#">
    <div class="card-photo" role="img" aria-label="Keyboard and notebook with hands writing"></div>
    <div class="card-frame">
      <h2 class="card-title">Business</h2>
      <p class="card-text">Lorem ipsum dolor sit amet, consectetuer adipiscing elit. Aenean commodo ligula eget dolor.</p>
    </div>
  </a>
</div>
</body>
</html>
```